Vellandor Insurance & Consulting

We need a new business card designed.
Front Side:
Photo on left
Logo on top right
Name, title, company, and contact info aligned on right
Clean spacing with professional hierarchy

Back Side:
Tagline centered near the top:
Real expertise. Practical guidance. Reliable protection.

Coverage types centered below in 2 lines:
General Liability | Workers Comp | Commercial Auto
Property | Inland Marine | Excess Liability | Pollution

```html
<!DOCTYPE html>
<html lang="en">
<head>
<meta charset="utf-8">
<title>Vellandor Insurance &amp; Consulting – Business Card</title>
<link rel="stylesheet" href="https://fonts.googleapis.com/css2?family=Oswald:wght@400;500&family=Montserrat:wght@400&family=Open+Sans:wght@400&display=swap">
<style>
  :root {
    --page-bg: #dedede;
    --card-light: #ffffff;
    --card-dark: #000000;
    --ink: #111111;
    --ink-muted: #6f6f6f;
    --ink-soft: #7c7c7c;
    --coverage: #9a9a9a;
    --paper-white: #ffffff;
    --photo-dark: #2a2d3d;
    --photo-mid: #6b5a52;
    --photo-light: #cfc8c4;
  }
  * { margin: 0; padding: 0; box-sizing: border-box; }
  html, body {
    width: 1200px; height: 1000px; overflow: hidden;
    background: var(--page-bg);
  }
  .sheet {
    position: relative; width: 1200px; height: 1000px;
    display: flex; flex-direction: column; align-items: center; justify-content: center; gap: 50px;
  }
  .card {
    position: relative; width: 780px; height: 450px;
    border-radius: 34px; overflow: hidden;
  }
  .card--front { background: var(--card-light); }
  .card--back { background: var(--card-dark); }

  /* Front */
  .portrait {
    position: absolute; left: 108px; top: 0; width: 262px; height: 450px;
    background: linear-gradient(180deg, var(--photo-mid) 0%, var(--photo-light) 22%, var(--photo-dark) 45%, var(--photo-dark) 100%);
    opacity: 0.9;
  }
  .front-info {
    position: absolute; right: 90px; top: 36px; width: 360px; text-align: right;
  }
  .brand-mark {
    display: inline-flex; align-items: center; gap: 10px;
    font-family: "Oswald", sans-serif; font-weight: 500; color: var(--ink);
    font-size: 24px; line-height: 1.05; text-align: left;
  }
  .brand-mark__dot { width: 36px; height: 36px; border-radius: 50%; background: var(--ink); flex: none; }
  .brand-mark small { display: block; font-size: 15px; font-weight: 500; }
  .person-name {
    margin-top: 30px;
    font-family: "Oswald", sans-serif; font-weight: 500; font-size: 40px; line-height: 1.1; color: var(--ink);
  }
  .person-title {
    font-family: "Oswald", sans-serif; font-weight: 400; font-size: 24px; color: var(--ink-muted);
  }
  .contact {
    margin-top: 70px;
    font-family: "Montserrat", sans-serif; font-size: 18px; line-height: 1.35; color: var(--ink-soft);
  }
  .contact__phone { display: inline-flex; align-items: center; gap: 4px; }
  .contact__phone svg { width: 13px; height: 13px; }
  .address {
    margin-top: 32px; margin-right: -4px;
    font-family: "Montserrat", sans-serif; font-size: 15.5px; line-height: 1.3; color: var(--ink-soft);
  }

  /* Back */
  .back-brand {
    position: absolute; left: 100px; top: 190px;
    display: flex; align-items: center; gap: 14px;
    font-family: "Oswald", sans-serif; font-weight: 500; color: var(--paper-white);
    font-size: 38px; line-height: 1.05;
  }
  .back-brand__dot { width: 56px; height: 56px; border-radius: 50%; background: var(--paper-white); flex: none; }
  .back-brand small { display: block; font-size: 20px; font-weight: 500; }
  .tagline {
    position: absolute; left: 449px; top: 146px;
    font-family: "Oswald", sans-serif; font-weight: 500; font-size: 30px; line-height: 40px; color: var(--paper-white);
  }
  .coverage {
    position: absolute; left: 0; right: 0; top: 336px; text-align: center;
    font-family: "Open Sans", sans-serif; font-size: 23px; line-height: 37px; color: var(--coverage);
  }
</style>
</head>
<body>
<main class="sheet">
  <section class="card card--front" aria-label="Business card front">
    <div class="portrait" role="img" aria-label="Portrait photo of the agency principal in a navy polka-dot dress"></div>
    <div class="front-info">
      <div class="brand-mark">
        <span class="brand-mark__dot"></span>
        <span>Vellandor<small>Insurance &amp; Consulting</small></span>
      </div>
      <h1 class="person-name">Marisol Vantreco</h1>
      <p class="person-title">Agency Principal</p>
      <div class="contact">
        <p class="contact__phone">
          <svg viewBox="0 0 24 24" aria-hidden="true"><path fill="#111" d="M6.6 10.8a15.1 15.1 0 0 0 6.6 6.6l2.2-2.2a1 1 0 0 1 1-.25 11.4 11.4 0 0 0 3.6.57 1 1 0 0 1 1 1V20a1 1 0 0 1-1 1A17 17 0 0 1 3 4a1 1 0 0 1 1-1h3.5a1 1 0 0 1 1 1c0 1.25.2 2.45.57 3.57a1 1 0 0 1-.25 1z"/></svg>
          (503) 555-0147
        </p>
        <p>admin@vellandorins.com</p>
      </div>
      <address class="address" style="font-style:normal">
        4120 SW Alderbrook Ave Suite 210<br>Fairhaven, Oregon 97000
      </address>
    </div>
  </section>

  <section class="card card--back" aria-label="Business card back">
    <div class="back-brand">
      <span class="back-brand__dot"></span>
      <span>Vellandor<small>Insurance &amp; Consulting</small></span>
    </div>
    <p class="tagline">Real expertise.<br>Practical guidance.<br>Reliable protection.</p>
    <p class="coverage">
      General Liability | Workers Comp | Commercial Auto<br>
      Property | Inland Marine | Excess Liability | Pollution
    </p>
  </section>
</main>
</body>
</html>
```